Business Card Design Project

I require a business card with the following information on them for various different people;
name
m:
f:
e:
I have a logo already and will attached that. We are in the construction industry. I require something clean and simple but eye catching at the same time. You can use another colour with our logo if you like and you can style the logo as well if you wish. I am open.
Also it needs to be front and back design.
Industry/Entity Type
Construction
Requirements
Must have
- Logo, name, mobile, fax and email address.
Front and back design

```html
<!DOCTYPE html>
<html lang="en">
<head>
<meta charset="utf-8">
<title>Northgate Builds — Business Cards</title>
<link rel="stylesheet" href="https://fonts.googleapis.com/css2?family=Open+Sans:wght@400;700&display=swap">
<style>
  :root {
    --stage: #000000;
    --paper: #ffffff;
    --green-deep: #4aa944;
    --green-mid: #8cc63f;
    --green-light: #b8da5c;
    --ink: #2b2b2b;
  }
  html, body {
    margin: 0;
    padding: 0;
    width: 1200px;
    height: 900px;
    overflow: hidden;
    background: var(--stage);
    font-family: "Open Sans", Arial, sans-serif;
  }
  .stage {
    position: relative;
    width: 1200px;
    height: 900px;
  }
  .card {
    position: absolute;
    left: 348px;
    width: 504px;
    height: 288px;
    overflow: hidden;
    background: var(--paper);
  }
  .card--front { top: 111px; }
  .card--back { top: 500px; }
  .card__art {
    position: absolute;
    inset: 0;
    width: 504px;
    height: 288px;
  }
  .brand {
    position: absolute;
    left: 20px;
    display: flex;
    align-items: center;
    gap: 9px;
  }
  .card--front .brand { top: 238px; }
  .card--back .brand { top: 16px; }
  .brand__mark {
    width: 26px;
    height: 26px;
    background: var(--green-deep);
  }
  .brand__name {
    font-size: 27px;
    font-weight: 400;
    color: var(--green-deep);
    letter-spacing: -0.3px;
    line-height: 1;
  }
  .person {
    position: absolute;
    left: 23px;
    top: 243px;
    margin: 0;
    font-size: 21px;
    font-weight: 700;
    color: var(--paper);
  }
  .contact {
    position: absolute;
    left: 316px;
    top: 218px;
    margin: 0;
    font-family: Arial, Helvetica, sans-serif;
    font-size: 13px;
    line-height: 16.5px;
    color: var(--ink);
    display: grid;
    grid-template-columns: 72px auto;
  }
  .contact dt, .contact dd { margin: 0; }
  .contact .contact__email { grid-column: 1 / 3; }
</style>
</head>
<body>
<main class="stage">
  <section class="card card--front" aria-label="Card front">
    <svg class="card__art" viewBox="0 0 504 288" aria-hidden="true">
      <defs>
        <linearGradient id="front-field" x1="0" y1="1" x2="1" y2="0">
          <stop offset="0" stop-color="var(--green-deep)"/>
          <stop offset="0.55" stop-color="var(--green-mid)"/>
          <stop offset="1" stop-color="var(--green-light)"/>
        </linearGradient>
      </defs>
      <rect width="504" height="288" fill="url(#front-field)"/>
      <polygon points="0,218 262,218 334,288 0,288" fill="var(--paper)"/>
    </svg>
    <div class="brand">
      <span class="brand__mark"></span>
      <span class="brand__name">Northgate Builds</span>
    </div>
  </section>

  <section class="card card--back" aria-label="Card back">
    <svg class="card__art" viewBox="0 0 504 288" aria-hidden="true">
      <defs>
        <linearGradient id="back-band" x1="0" y1="1" x2="1" y2="0">
          <stop offset="0" stop-color="var(--green-deep)"/>
          <stop offset="0.6" stop-color="var(--green-mid)"/>
          <stop offset="1" stop-color="var(--green-light)"/>
        </linearGradient>
      </defs>
      <polygon points="0,218 218,218 288,288 0,288" fill="url(#back-band)"/>
    </svg>
    <div class="brand">
      <span class="brand__mark"></span>
      <span class="brand__name">Northgate Builds</span>
    </div>
    <p class="person">First Lastname</p>
    <dl class="contact">
      <dt>mobile</dt><dd>123-4567</dd>
      <dt>fax</dt><dd>123-6789</dd>
      <dd class="contact__email">firstlastname@northgate.com</dd>
    </dl>
  </section>
</main>
</body>
</html>
```